University of Carrowind Larkmoor Saxophone Quartet Concert

We need a poster design advertising the Larkmoor Saxophone Quartet Concert on Tuesday, April 23 at 5pm. The program concert will consist of 2 works by Peter Oskivar: Harbor Lanterns and Vesper ledger. These two works should be included on the poster being the concert is featuring the composer and his works. Peter Oskivar is known for his very "natural" sounding music. He resides in Montana and writes mostly from his small cottage in the mountains. This same idea of nature and "Montana" should be included on the poster design. He is deeply influenced by Telvane and most of the music he writes is play offs from Telvane Chorales.

The concert title is: "Where Quiet Rivers Meet"

Target Market(s)

Collegiate Musician, Professional Musicians, Music Faculty

Industry/Entity Type

Advertising

Requirements
Must have
• 1. Title of the Concert: "Where Quiet Rivers Meet"
2. "Larkmoor Saxophone Quartet Presents"
3. Date (April 23)
4. Time: 5pm
5. Location: Chapel of The Blessed Orrin
Nice to have
• Nice to maybe keep the idea of "Montana" and that mountian-esque feel

```html
<!DOCTYPE html>
<html lang="en">
<head>
<meta charset="utf-8">
<title>Larkmoor Saxophone Quartet — Where Quiet Rivers Meet</title>
<link rel="stylesheet" href="https://fonts.googleapis.com/css2?family=Cinzel:wght@400&family=Oswald:wght@400;500&family=Playfair+Display:wght@400&display=swap">
<style>
  :root {
    --paper: #ffffff;
    --band: #231f20;
    --rule: #c9c9c9;
    --ink-light: #ffffff;
    --navy: #1c2c47;
    --sky: #3f7fd0;
    --rock: #7d8088;
    --lake: #3f8f93;
    --forest: #3d6b2c;
    --meadow: #5c8a35;
  }
  * { margin: 0; padding: 0; box-sizing: border-box; }
  html, body { width: 900px; height: 1200px; overflow: hidden; background: var(--paper); }
  .poster { position: relative; width: 900px; height: 1200px; background: var(--paper); }

  .header-rule { position: absolute; left: 0; width: 900px; height: 8px; background: var(--rule); }
  .header-rule.top { top: 50px; }
  .header-rule.bottom { top: 336px; }

  .header-band {
    position: absolute; left: 0; top: 58px; width: 900px; height: 278px;
    background: var(--band); color: var(--ink-light);
  }
  .ensemble-name {
    position: absolute; left: 56px; top: 26px;
    font-family: "Cinzel", serif; font-weight: 400;
    font-size: 66px; line-height: 76px; letter-spacing: 0.5px;
  }
  .program {
    position: absolute; right: 45px; top: 30px; text-align: right;
    font-family: "Oswald", sans-serif; font-weight: 500; text-transform: uppercase;
  }
  .program .composer { font-size: 25px; line-height: 34px; letter-spacing: 0.5px; }
  .program .work { font-size: 43px; line-height: 48px; }
  .program .work small { font-size: 25px; }
  .presents {
    position: absolute; right: 45px; top: 222px;
    font-family: "Cinzel", serif; font-size: 20px; letter-spacing: 10px;
  }

  .landscape-figure {
    position: absolute; left: 88px; top: 370px; width: 420px; height: 790px;
    border-radius: 180px 180px 40px 40px;
    background: linear-gradient(180deg, var(--sky) 0%, var(--sky) 16%, var(--rock) 34%, var(--lake) 50%, var(--forest) 66%, var(--meadow) 100%);
  }

  .concert-title {
    position: absolute; left: 490px; top: 378px; width: 380px; text-align: center;
    font-family: "Playfair Display", serif; font-weight: 400; color: var(--navy);
    font-size: 104px; line-height: 96px; letter-spacing: -5px; text-transform: uppercase;
    transform: scaleX(0.82); transform-origin: center top;
  }

  .details {
    position: absolute; right: 45px; text-align: right;
    font-family: "Oswald", sans-serif; font-weight: 400; color: var(--band);
    font-size: 40px; line-height: 48px; text-transform: uppercase;
  }
  .details.when { top: 925px; }
  .details.where { top: 1050px; }
</style>
</head>
<body>
<main class="poster">
  <div class="header-rule top"></div>
  <header class="header-band">
    <h1 class="ensemble-name">Larkmoor<br>Saxophone<br>Quartet</h1>
    <div class="program">
      <p class="composer">2 works by Peter Oskivar</p>
      <p class="work">Harbor Lanterns</p>
      <p class="work"><small>and</small> Vesper Ledger</p>
    </div>
    <p class="presents">Presents</p>
  </header>
  <div class="header-rule bottom"></div>

  <div class="landscape-figure" role="img" aria-label="Silhouette of a saxophonist filled with a Montana mountain landscape of blue sky, rocky peak, lake and pine forest"></div>

  <h2 class="concert-title">Where<br>Quiet<br>Rivers<br>Meet</h2>

  <p class="details when">April 23<br>at 5 PM</p>
  <p class="details where">Chapel of the<br>Blessed Orrin</p>
</main>
</body>
</html>
```